Customer Dashboard Design for Email Security SaaS

Mailbrook is a commercial email spam filter offered as a SaaS product, built and operated by a small German hosting provider. It protects business email accounts against spam, phishing, scam, and viruses using a multilayer filtering pipeline that combines traditional spam detection with AI-powered classification. The product runs entirely on German infrastructure, ensuring data sovereignty for European customers.

We need a complete redesign of the customer-facing dashboard. This is the web application where paying customers manage their email filtering: view their mail log, check quarantined emails, manage allow/blocklists, configure their settings, and handle their subscription. It is the primary touchpoint between Mailbrook and its customers.

Our customers are system administrators, IT managers at small-to-medium businesses, and operators of small hosting providers. They are technically competent but not designers. They expect professional, efficient tools that respect their time. They typically manage 10–500 email accounts and check the dashboard a few times per week, with heavier use during spam incidents.

We have attached the current mockups which really need to be replaced with something good looking.

Target Market(s)

System administrators, IT managers at small-to-medium businesses, and operators of small hosting providers.

Industry/Entity Type

SaaS

Number of Pages Required

5+ page

```html
<!DOCTYPE html>
<html lang="en">
<head>
<meta charset="utf-8">
<title>Mailbrook — Overview</title>
<link href="https://fonts.googleapis.com/css2?family=Inter:wght@400;500;600;700&family=JetBrains+Mono:wght@400;500;600&display=swap" rel="stylesheet">
<style>
:root{
  --bg:#121110;
  --panel:#1c1b19;
  --panel-2:#161513;
  --row:#121211;
  --line:#2e2c29;
  --text:#ecebe8;
  --muted:#b9b6b0;
  --accent:#e9a94b;
  --green:#3fb86a;
  --green-bg:#173423;
  --red:#e0524a;
  --red-bg:#3a1c1a;
  --amber-bg:#3b2c15;
  --sans:'Inter',sans-serif;
  --mono:'JetBrains Mono',monospace;
}
*{box-sizing:border-box;margin:0;padding:0}
html,body{width:1200px;height:882px;overflow:hidden;background:var(--bg);color:var(--text);font-family:var(--sans)}
.canvas{position:relative;width:1200px;height:882px}
.panel{position:absolute;background:var(--panel);border-radius:12px}
.mono{font-family:var(--mono)}

/* sidebar */
.sidebar{left:19px;top:20px;width:178px;height:842px}
.brand{position:absolute;left:20px;top:22px;display:flex;align-items:center;gap:7px;font-weight:700;font-size:19px}
.brand-mark{width:33px;height:33px;border-radius:8px;background:var(--accent)}
.nav{position:absolute;left:10px;top:97px;width:158px;list-style:none}
.nav li{display:flex;align-items:center;gap:12px;height:40px;margin-bottom:11.7px;padding-left:10px;font-size:12.5px}
.nav li svg{width:17px;height:17px;stroke:var(--text);fill:none;stroke-width:1.6}
.nav li.active{border:1.5px solid var(--accent);border-top:none;border-radius:8px;color:var(--accent);font-size:13.5px;background:#1d1a15}
.nav li.active svg{stroke:var(--accent)}
.side-rule{position:absolute;left:10px;right:10px;top:526px;border-top:1px solid var(--line)}
.admin-label{position:absolute;left:10px;top:563px;font-size:10.5px;font-weight:500}
.admin-link{position:absolute;left:10px;font-size:12px;display:flex;align-items:center;gap:10px}
.audit{position:absolute;left:10px;top:678px;width:158px;height:40px;border-radius:7px;background:var(--accent);color:#1a140a;font-family:var(--mono);font-weight:600;font-size:14px;display:flex;align-items:center;justify-content:center}
.logout{position:absolute;left:55px;top:793px;font-size:12.5px;display:flex;align-items:center;gap:10px}

/* hero */
.hero{left:217px;top:20px;width:668px;height:220px;overflow:hidden;background:radial-gradient(circle at 95% -10%,#2a2824 0,#1c1b19 40%)}
.hero h1{position:absolute;left:20px;top:22px;color:var(--accent);font-size:34px;font-weight:600;letter-spacing:.2px}
.hero-meta{position:absolute;left:20px;top:82px;font-size:15px;color:var(--muted);display:flex;gap:14px;align-items:center}
.dot{width:8px;height:8px;border-radius:50%;background:var(--green);display:inline-block;margin-right:8px}
.stat{position:absolute;top:127px;height:75px;border:1px solid var(--line);border-radius:7px;background:var(--panel-2);padding:10px 10px}
.stat b{display:block;font-family:var(--mono);font-weight:500;font-size:29px;line-height:1.1}
.stat span{font-family:var(--mono);font-size:13px;color:var(--muted)}

/* billing */
.billing{left:905px;top:20px;width:275px;height:220px;padding:0 20px}
.billing h2{position:absolute;left:17px;top:30px;font-size:24px;font-weight:600}
.tag{font-family:var(--mono);font-size:9.5px;padding:3px 8px;border-radius:3px}
.tag.green{background:var(--green-bg);color:var(--green)}
.tag.red{background:var(--red-bg);color:var(--red)}
.tag.amber{background:var(--amber-bg);color:var(--accent)}
.billing .tag{position:absolute;right:20px;top:35px}
.b-label{position:absolute;font-weight:600;font-size:13.5px}
.b-small{position:absolute;font-family:var(--mono);font-size:10.5px;color:var(--muted)}

/* mail log */
.maillog{left:217px;top:260px;width:570px;height:360px}
.panel-title{position:absolute;left:17px;top:22px;font-size:21px;font-weight:500}
.link{position:absolute;font-family:var(--mono);font-size:12px;color:var(--accent)}
.log-table{position:absolute;left:17px;top:82px;width:537px;border-collapse:collapse;font-family:var(--mono);font-size:12px}
.log-table th{font-family:var(--sans);font-weight:500;font-size:12px;text-align:left;height:37px}
.log-table td{height:49px}
.log-table tr.first td{height:33px;background:var(--row)}
.log-table tr.first td:first-child{border-radius:5px 0 0 5px;padding-left:7px}
.log-table tr.first td:last-child{border-radius:0 5px 5px 0;padding-right:7px}
.log-table .r{text-align:right}

/* quarantine */
.quarantine{left:807px;top:260px;width:373px;height:360px}
.q-sub{position:absolute;left:17px;top:57px;font-family:var(--mono);font-size:12px;color:var(--muted)}
.q-item{position:absolute;left:17px;width:339px;height:72px;border-radius:10px;background:var(--panel-2);padding:16px 16px}
.q-item small{display:block;font-family:var(--mono);font-size:9.5px;color:var(--muted);margin-bottom:7px}
.q-item p{font-family:var(--mono);font-size:13.5px;letter-spacing:.3px}
.release{position:absolute;right:16px;top:22px;height:26px;padding:0 7px;border-radius:5px;background:var(--green-bg);color:var(--green);font-family:var(--mono);font-size:8px;display:flex;align-items:center;gap:6px}

/* lists */
.listpanel{top:640px;height:222px}
.listpanel h2{position:absolute;left:20px;top:26px;font-size:24px;font-weight:600;display:flex;align-items:center;gap:10px}
.list-sub{position:absolute;left:20px;top:69px;font-family:var(--mono);font-size:12px;color:var(--muted)}
.add{position:absolute;top:20px;width:101px;height:40px;border-radius:7px;background:var(--panel-2);color:var(--accent);font-family:var(--mono);font-size:12px;display:flex;align-items:center;justify-content:center;gap:10px}
.chip{position:absolute;left:21px;width:253px;height:28px;border-radius:3px;font-family:var(--mono);font-size:12px;display:flex;align-items:center;justify-content:space-between;padding:0 13px 0 17px}
.chip.allow{background:#1c2c20;color:var(--green)}
.chip.block{background:#2d1c1a;color:var(--text)}
.chip i{font-style:normal;color:var(--muted);font-size:13px}
.updated{position:absolute;top:170px;font-family:var(--mono);font-size:12px;line-height:1.2}
</style>
</head>
<body>
<div class="canvas">

  <aside class="panel sidebar">
    <div class="brand"><span class="brand-mark"></span>Mailbrook</div>
    <ul class="nav">
      <li class="active"><svg viewBox="0 0 24 24"><path d="M3 11l9-7 9 7v9h-6v-6H9v6H3z"/></svg>OVERVIEW</li>
      <li><svg viewBox="0 0 24 24"><rect x="3" y="5" width="18" height="12"/><path d="M3 9h18M3 20h18"/></svg>Mail-Log</li>
      <li><svg viewBox="0 0 24 24"><path d="M3 10l9-6 9 6v10H3z"/><path d="M3 10l9 6 9-6"/></svg>Mail-Box</li>
      <li><svg viewBox="0 0 24 24"><path d="M12 3l8 3v6c0 5-4 8-8 9-4-1-8-4-8-9V6z"/><path d="M8.5 12l2.5 2.5 4.5-5"/></svg>Allowlist</li>
      <li><svg viewBox="0 0 24 24"><path d="M12 3l8 3v6c0 5-4 8-8 9-4-1-8-4-8-9V6z"/><path d="M12 8v5M12 16v.5"/></svg>Blocklist</li>
      <li><svg viewBox="0 0 24 24"><rect x="5" y="11" width="14" height="10" rx="1"/><path d="M8 11V7a4 4 0 018 0v4M12 15v2"/></svg>Quarantine</li>
      <li><svg viewBox="0 0 24 24"><circle cx="12" cy="12" r="3"/><path d="M12 2v3M12 19v3M2 12h3M19 12h3M4.9 4.9l2.1 2.1M17 17l2.1 2.1M4.9 19.1L7 17M17 7l2.1-2.1"/></svg>Settings</li>
      <li><svg viewBox="0 0 24 24"><rect x="3" y="6" width="18" height="12" rx="1"/><circle cx="12" cy="12" r="2.5"/></svg>Billing</li>
    </ul>
    <div class="side-rule"></div>
    <div class="admin-label">ADMINISTRATION</div>
    <div class="admin-link" style="top:603px">System Settings</div>
    <div class="admin-link" style="top:639px"><svg width="17" height="17" viewBox="0 0 24 24" fill="none" stroke="#ecebe8" stroke-width="1.6"><circle cx="12" cy="12" r="10"/><path d="M9.5 9a2.5 2.5 0 014.5 1.5c0 1.5-2 2-2 3.5M12 17v.5"/></svg><span style="margin-left:6px">Help Center</span></div>
    <div class="audit">Security Audit</div>
    <div class="logout"><svg width="17" height="17" viewBox="0 0 24 24" fill="none" stroke="#ecebe8" stroke-width="1.8"><path d="M10 4H4v16h6M14 8l4 4-4 4M18 12H9"/></svg>Log Out</div>
  </aside>

  <section class="panel hero">
    <h1>Good morning, Administrator</h1>
    <div class="hero-meta"><span>In Last 24 Hours</span><span>.</span><span>No critical threats detected</span><span style="margin-left:16px;color:var(--text)"><span class="dot"></span>Protection Active</span></div>
    <div class="stat" style="left:20px;width:147px"><b>212</b><span>Spam Blocked</span></div>
    <div class="stat" style="left:190px;width:188px"><b>28</b><span>Phishing Detected</span></div>
    <div class="stat" style="left:404px;width:147px"><b>40</b><span>Quarantine</span></div>
  </section>

  <section class="panel billing">
    <h2>Billing</h2>
    <span class="tag green">Active</span>
    <div class="b-small" style="left:17px;top:85px;font-size:12px;color:var(--text)">Your payment Information</div>
    <div class="b-label" style="left:17px;top:125px;color:var(--accent)">Enterprise Plan</div>
    <div class="b-small" style="left:17px;top:149px;color:var(--text)">$450.00/ monthly</div>
    <div class="b-label" style="left:17px;top:184px">Billing Cycle</div>
    <div class="b-label" style="left:143px;top:186px">Payment Method</div>
    <div class="b-small" style="left:17px;top:209px">Monthly</div>
    <div class="b-small" style="left:143px;top:209px">Invoice</div>
  </section>

  <section class="panel maillog">
    <h2 class="panel-title">Mail Log</h2>
    <a class="link" style="right:17px;top:27px">View Full Logs</a>
    <table class="log-table">
      <tr><th style="width:180px">Sender</th><th style="width:182px">Subject</th><th>Status</th><th class="r">Reason</th></tr>
      <tr class="first"><td>Smith@company-inc.com</td><td>Invoice #1234 attached</td><td><span class="tag green">Deliverd</span></td><td class="r">AllowListed</td></tr>
      <tr><td>no-reply@crypto-win.io</td><td>Claim your Rewards</td><td><span class="tag red">Blocked</span></td><td class="r">Phishing</td></tr>
      <tr><td>j.Smith@company-inc.com</td><td>Invoice #1234 attached</td><td><span class="tag amber">Qurantined</span></td><td class="r">AllowListed</td></tr>
      <tr><td>j.Smith@company-inc.com</td><td>Invoice #1234 attached</td><td><span class="tag green">Deliverd</span></td><td class="r">AllowListed</td></tr>
      <tr><td>marketingTrends.com</td><td>Top 10 Stretagy for work</td><td><span class="tag red">Blocked</span></td><td class="r">Phishing</td></tr>
    </table>
  </section>

  <section class="panel quarantine">
    <h2 class="panel-title">40 emails in quarantine</h2>
    <a class="link" style="right:17px;top:27px">Review All</a>
    <div class="q-sub">Suspicious mail store here...</div>
    <div class="q-item" style="top:111px"><small>j.Smith@company-inc.com</small><p>Invoice #1234 attached...</p><span class="release">⇡ Release Emails</span></div>
    <div class="q-item" style="top:191px"><small>Parker@partner348.com</small><p>Invoice #2281 attached...</p><span class="release">⇡ Release Emails</span></div>
    <div class="q-item" style="top:271px"><small>j.Smith@company-inc.com</small><p>Invoice #1234 attached...</p><span class="release">⇡ Release Emails</span></div>
  </section>

  <section class="panel listpanel" style="left:217px;width:471px">
    <h2>AllowList <svg width="20" height="20" viewBox="0 0 24 24" fill="none" stroke="#3fb86a" stroke-width="2"><circle cx="12" cy="12" r="9" stroke-dasharray="4 2"/><path d="M8 12l3 3 5-6"/></svg></h2>
    <div class="list-sub">Trusted People</div>
    <div class="add" style="right:20px"><span style="font-size:17px">+</span>Add New</div>
    <div class="chip allow" style="top:102px">Smith@company-inc.com<i>✕</i></div>
    <div class="chip allow" style="top:137px">Paywell@company-inc.com<i>✕</i></div>
    <div class="chip allow" style="top:172px">billing@striva-inc.com<i>✕</i></div>
    <div class="updated" style="left:351px">Last updated<br>2 days ago</div>
  </section>

  <section class="panel listpanel" style="left:708px;width:472px">
    <h2>BlockedList <svg width="20" height="20" viewBox="0 0 24 24" fill="none" stroke="#e0524a" stroke-width="2.2"><circle cx="12" cy="12" r="9"/><path d="M5.6 5.6l12.8 12.8"/></svg></h2>
    <div class="list-sub">Blocked People</div>
    <div class="add" style="right:20px"><span style="font-size:17px">+</span>Add New</div>
    <div class="chip block" style="top:102px">no-reply@crypto-win.io<i>✕</i></div>
    <div class="chip block" style="top:137px">marketingTrends<i>✕</i></div>
    <div class="chip block" style="top:172px">no-reply@crypto-win.io<i>✕</i></div>
    <div class="updated" style="left:353px">Last updated<br>6 hours ago</div>
  </section>

</div>
</body>
</html>
```